cutest and professional business cards

I am looking at getting very good designs that will scream - contact this TEAM (7)
So could be that one or two awesome design and in variations for members of my team. Vector files are attached within the brief.
I will like the circle image (see vector-file) to be within the back of the cards as part of the design and the text "You're Creative - Join our Community"

Target Market(s)

Creative youths and millennials as well as very business/entrepreneurial minded community.

Contact Information for Business Card

logo,
name: for design1: Marlene Ikpefa for design2,3,4,5,6,7: leave blank space to possibility to handprint/sign name
position: design1: Founder, design2,3,4,5,6,7: community relationship manager, Fullstack developer, software designer, digital marketer, financial and operating officer, creative intern
address: Tendrilhub - 42 Wexmoor Ave Nepean ON k4r 3x2
number: 613-4289-517
website: www.fyrolume.com
linkedin -/fyrolum
facebook - /fyrolum
twitter - /fyrolu
instagram -/fyrolum

Font styles to use
Other font styles liked:
• monserratt

Requirements
Must have
• Font type: monserratt
• colours: off blue #1BBC9C , Red #BB2838
Nice to have
• a catchy, youthful and professional design
Should not have
• any additional colors besides dark grey and white.

```html
<!DOCTYPE html>
<html lang="en">
<head>
<meta charset="UTF-8">
<title>Fyrolume Business Cards</title>
<link rel="stylesheet" href="https://fonts.googleapis.com/css2?family=Montserrat:wght@400;500;700&family=Lato:wght@400;700&display=swap">
<style>
  :root {
    --teal: #1BBC9C;
    --red: #BB2838;
    --charcoal: #333335;
    --ink: #2b2b2d;
    --grey-text: #4a4a4c;
    --paper: #ffffff;
    --backdrop: #e6e6e8;
  }
  * { box-sizing: border-box; margin: 0; padding: 0; }
  html, body {
    width: 1200px; height: 880px; overflow: hidden;
    background: var(--backdrop);
  }
  .canvas { position: relative; width: 1200px; height: 880px; }
  .card {
    position: absolute; width: 520px; height: 297px;
    box-shadow: 0 10px 28px rgba(0,0,0,0.22);
    overflow: hidden;
  }
  .card-front { left: 90px; top: 120px; background: var(--charcoal); }
  .card-back { left: 590px; top: 463px; background: var(--paper); }

  .wordmark {
    position: absolute;
    display: flex; align-items: center; gap: 10px;
    font-family: "Montserrat", sans-serif;
    font-weight: 700; letter-spacing: 0.5px;
    white-space: nowrap;
  }
  .wordmark-dot {
    width: 26px; height: 26px; border-radius: 50%;
    background: var(--teal); flex: none;
  }
  .card-front .wordmark {
    left: 50%; top: 120px; transform: translate(-50%, -50%);
    font-size: 46px; color: var(--paper);
  }
  .tagline {
    position: absolute; left: 0; right: 0; top: 170px;
    text-align: center;
    font-family: "Montserrat", sans-serif;
    font-weight: 500; font-size: 14px; letter-spacing: 0.6px;
    color: var(--teal);
  }
  .card-back .wordmark {
    left: 30px; top: 124px;
    font-size: 32px; color: var(--ink);
  }
  .card-back .wordmark-dot { width: 20px; height: 20px; }

  .divider {
    position: absolute; left: 262px; top: 40px;
    width: 1.5px; height: 200px; background: var(--teal);
  }
  .contact {
    position: absolute; left: 288px; top: 30px; right: 20px;
    font-family: "Lato", sans-serif; color: var(--grey-text);
  }
  .contact-name {
    font-family: "Montserrat", sans-serif;
    font-weight: 700; font-size: 18px; color: var(--red);
    line-height: 1.1;
  }
  .contact-role { font-size: 12.5px; margin-bottom: 10px; }
  .contact-row {
    display: flex; align-items: center; gap: 6px;
    font-size: 12.5px; line-height: 18px;
  }
  .contact-icon { width: 14px; height: 14px; flex: none; }
  .contact-address { font-size: 12.5px; line-height: 16px; margin-top: 8px; }
  .social-list {
    display: grid; grid-template-columns: repeat(2, auto);
    justify-content: start; column-gap: 22px; row-gap: 2px;
    margin-top: 10px; font-size: 12px; line-height: 16px;
    list-style: none;
  }
  .social-item { display: flex; align-items: center; gap: 6px; }
  .social-mark {
    width: 7px; height: 7px; background: var(--teal); flex: none;
  }

  .base-band {
    position: absolute; left: 0; bottom: 0; width: 100%; height: 14px;
    display: flex;
  }
  .band-dark { flex: 1; background: var(--charcoal); }
  .band-teal { width: 76px; background: var(--teal); }
  .band-red { width: 76px; background: var(--red); }
</style>
</head>
<body>
<main class="canvas">

  <section class="card card-front" aria-label="Card front">
    <div class="wordmark">
      <span class="wordmark-dot"></span>
      <span class="wordmark-name">Fyrolume</span>
    </div>
    <p class="tagline">You're Creative - Join our Community</p>
  </section>

  <section class="card card-back" aria-label="Card back">
    <div class="wordmark">
      <span class="wordmark-dot"></span>
      <span class="wordmark-name">Fyrolume</span>
    </div>

    <div class="divider"></div>

    <div class="contact">
      <p class="contact-name">Marlene Ikpefa</p>
      <p class="contact-role">Founder</p>

      <p class="contact-row">
        <svg class="contact-icon" viewBox="0 0 14 14" aria-hidden="true">
          <circle cx="7" cy="7" r="7" fill="var(--red)"/>
          <path d="M4.3 3.6c.4-.3.9-.3 1.1.1l.6 1.1c.2.3.1.7-.2.9l-.4.3c.4.9 1.1 1.6 2 2l.3-.4c.2-.3.6-.4.9-.2l1.1.6c.4.2.4.7.1 1.1-.6.7-1.4.8-2.3.4C6 8.8 5.2 8 4.5 6.7c-.5-1-.6-2.3-.2-3.1z" fill="#fff"/>
        </svg>
        613-4289-517
      </p>
      <p class="contact-row">
        <svg class="contact-icon" viewBox="0 0 14 14" aria-hidden="true">
          <circle cx="7" cy="7" r="7" fill="var(--red)"/>
          <rect x="3.5" y="4.6" width="7" height="4.8" fill="#fff"/>
          <path d="M3.5 4.6 7 7.4l3.5-2.8" fill="none" stroke="var(--red)" stroke-width="0.8"/>
        </svg>
        info@fyrolume.com
      </p>
      <p class="contact-row">
        <svg class="contact-icon" viewBox="0 0 14 14" aria-hidden="true">
          <circle cx="7" cy="7" r="7" fill="var(--red)"/>
          <circle cx="7" cy="7" r="3.6" fill="none" stroke="#fff" stroke-width="0.9"/>
          <ellipse cx="7" cy="7" rx="1.5" ry="3.6" fill="none" stroke="#fff" stroke-width="0.8"/>
          <path d="M3.4 7h7.2" stroke="#fff" stroke-width="0.8"/>
        </svg>
        www.fyrolume.com
      </p>

      <p class="contact-address">Tendrilhub - 42 Wexmoor Ave<br>Nepean ON k4r 3x2</p>

      <ul class="social-list">
        <li class="social-item"><span class="social-mark"></span>/fyrolum</li>
        <li class="social-item"><span class="social-mark"></span>/fyrolum</li>
        <li class="social-item"><span class="social-mark"></span>/fyrolu</li>
        <li class="social-item"><span class="social-mark"></span>/fyrolum</li>
      </ul>
    </div>

    <div class="base-band">
      <span class="band-dark"></span>
      <span class="band-teal"></span>
      <span class="band-red"></span>
    </div>
  </section>

</main>
</body>
</html>
```